A new presentation to our clients

we are a Real Estate agency, our website is www.dorelumia.com and it’s time to have a new, fashion and remarcable Business Card. we want to differentiate ourselves from other companies so we want a business card that differentiates us. we want the business card to impact our customers. in the competitive market that we have today, we have to be different and it is this difference that we seek

Target Market(s)

Real Estate Clients

Contact Information for Business Card

We search a totaly diferent card from the usual

Font styles to use
Sans Serif

Colors
e34197

Requirements
Must have
• Logo, adress, phone contact, e-mail, photo, and our website
Nice to have
• We would like to see a modern business card
Should not have
• Houses or building draws

```html
<!DOCTYPE html>
<html lang="pt">
<head>
<meta charset="utf-8">
<title>Dore Lumia — Business Card</title>
<link href="https://fonts.googleapis.com/css2?family=Montserrat:wght@500;600;700&display=swap" rel="stylesheet">
<style>
  :root {
    --brand-pink: #e3196f;
    --brand-pink-deep: #c8145f;
    --brand-pink-light: #ec2a82;
    --white: #ffffff;
    --stage: #ececec;
    --photo-light: #e6e8e3;
    --photo-mid: #b3b1b0;
    --photo-dark: #7e7b7c;
  }
  * { box-sizing: border-box; margin: 0; padding: 0; }
  html, body { width: 1200px; height: 900px; overflow: hidden; }
  body {
    background: var(--stage);
    font-family: "Montserrat", Arial, sans-serif;
    position: relative;
  }
  .card {
    position: absolute;
    left: 300px;
    width: 600px;
    height: 340px;
    border-radius: 22px;
    overflow: hidden;
    box-shadow: 0 10px 28px rgba(0,0,0,0.18);
  }
  .card--front {
    top: 90px;
    background: linear-gradient(160deg, var(--brand-pink-light) 0%, var(--brand-pink) 55%, var(--brand-pink-deep) 100%);
    display: flex;
    align-items: center;
    justify-content: center;
  }
  .brand-name {
    font-weight: 700;
    letter-spacing: 0.5px;
    line-height: 1;
    white-space: nowrap;
  }
  .card--front .brand-name { color: var(--white); font-size: 46px; }
  .card--back { top: 470px; }
  .room-photo {
    position: absolute;
    inset: 0;
    background: linear-gradient(110deg, var(--photo-light) 0%, var(--photo-light) 18%, var(--photo-mid) 45%, var(--photo-dark) 100%);
  }
  .card--back .brand-name {
    position: absolute;
    left: 40px;
    top: 116px;
    color: var(--brand-pink);
    font-size: 40px;
  }
  .contact-panel {
    position: absolute;
    right: 0;
    top: 152px;
    width: 232px;
    background: var(--brand-pink);
    color: var(--white);
    padding: 12px 14px 14px;
    font-size: 13px;
    font-weight: 500;
    font-style: normal;
    line-height: 1.35;
  }
  .contact-address { padding-bottom: 6px; border-bottom: 1px solid rgba(255,255,255,0.7); margin-bottom: 6px; }
  .contact-list { list-style: none; }
  .contact-list li { display: flex; align-items: center; gap: 6px; }
  .contact-icon { width: 12px; height: 12px; flex: none; }
</style>
</head>
<body>
  <section class="card card--front">
    <span class="brand-name">Dore Lumia</span>
  </section>

  <section class="card card--back">
    <div class="room-photo" role="img" aria-label="Photo of a modern living room with a dark sectional sofa, framed pictures on a grey wall and a bright window"></div>
    <span class="brand-name">Dore Lumia</span>
    <address class="contact-panel">
      <p class="contact-address">Rua das Camélias, 48<br>4100-210, Porto Velho</p>
      <ul class="contact-list">
        <li>
          <svg class="contact-icon" viewBox="0 0 12 12"><path d="M3 1 L5 3.5 L4 5 Q5 7 7 8 L8.5 7 L11 9 L9.5 11 Q4 10.5 1 3 Z" fill="#fff"/></svg>
          (+351) 210 555 048
        </li>
        <li>
          <svg class="contact-icon" viewBox="0 0 12 12"><rect x="0.5" y="2.5" width="11" height="7.5" fill="#fff"/><path d="M0.5 2.5 L6 7 L11.5 2.5" fill="none" stroke="#e3196f" stroke-width="1"/></svg>
          geral@dorelumia.com
        </li>
        <li>
          <svg class="contact-icon" viewBox="0 0 12 12"><circle cx="6" cy="6" r="5" fill="none" stroke="#fff" stroke-width="1.2"/><ellipse cx="6" cy="6" rx="2" ry="5" fill="none" stroke="#fff" stroke-width="1"/><line x1="1" y1="6" x2="11" y2="6" stroke="#fff" stroke-width="1"/></svg>
          www.dorelumia.com
        </li>
      </ul>
    </address>
  </section>
</body>
</html>
```